Create a 3-4 page concept for an electrical contracting company

We are a company that requires a new look for our website. We are familiar with Wordpress to be able to update using any theme or builder supplied.

While typical ideas of construction may get the yellow and blue colour pallette, hard hats, hammers, or lightning bolts entering the arena, we are completely against this image.

We intend for the website to have instant appeal and intuitive navigation. The home page should have a creative use of angles or brand identification with the banner or menubar if needed.

After combing hundreds of wordpress templates, the most attractive seem to be aimed at beauty services. Unfortunately we do not have a lot of picture perfect material to showcase, but it can be blended in other ways. - the brand should be recognizable and captivating.

Target Market(s)

High-end contracting firms focused on quality and service for long term projects (Custom Homes)

Industry/Entity Type

Contracting

Font styles to use
Sans Serif
Other font styles liked:
• Gotham usually. Adjusted kerning and rounded edges seem to be more friendly

Requirements
Must have
• Creative use of the logo shape and colour scheme, especially at the home.

Use of a CMS to be modifiable from a browser (Wordpress,etc) - A builder such as muffin, divi, or elementor accepted!

Elements or sections that could be adaptable for use. About us, members, contact, services... etc. Content would be written after
Nice to have
• Some clean inspiration that we appreciate:

www.marrowpixel.ca
www.ferndalebuildworks.com
Should not have
• Generic welcome banner...

```html
<!DOCTYPE html>
<html lang="en">
<head>
<meta charset="utf-8">
<title>Keystone Current — Electrical Contracting</title>
<link href="https://fonts.googleapis.com/css2?family=Montserrat:wght@400;500;600;700;800;900&display=swap" rel="stylesheet">
<style>
:root{
  --navy-deep:#060d1a;
  --navy:#0b1a2e;
  --navy-mid:#14304f;
  --accent:#2f7bb8;
  --accent-light:#4a9ad6;
  --btn:#1d557f;
  --btn-border:#6fa6d0;
  --light:#f2f2f3;
  --white:#ffffff;
  --text:#1d1d1f;
  --muted:#c9d6e4;
  --footer:#08101d;
}
*{margin:0;padding:0;box-sizing:border-box}
html,body{width:1200px;height:3673px;overflow:hidden}
body{position:relative;font-family:"Montserrat",sans-serif;color:var(--text);background:var(--light)}
.backdrop{position:absolute;left:0;top:0}
.abs{position:absolute}
.btn{position:absolute;display:flex;align-items:center;justify-content:center;height:46px;border-radius:23px;background:var(--btn);border:2px solid var(--btn-border);color:var(--white);font-size:15px;font-weight:600;letter-spacing:.5px}
/* top bar */
.topbar{font-size:13px;color:var(--muted);top:10px}
.topbar svg{vertical-align:-2px;margin-right:5px}
/* header */
.brand{left:160px;top:70px;display:flex;align-items:center;gap:14px}
.brand-mark{width:40px;height:40px;background:var(--accent)}
.brand-name{font-size:26px;font-weight:600;color:var(--accent-light);line-height:1;letter-spacing:1px;text-transform:uppercase;width:170px}
.nav{top:86px;left:557px;display:flex;gap:0;font-size:15px;color:var(--accent-light)}
.nav a{position:absolute;white-space:nowrap;text-decoration:none;color:inherit}
.nav .active{color:var(--accent-light)}
.nav .active::after{content:"";position:absolute;left:10px;right:10px;top:26px;height:3px;background:var(--white)}
/* hero */
.hero-kicker{width:1200px;text-align:center;top:280px;font-size:29px;font-weight:500;letter-spacing:2px;color:var(--white)}
.hero-title{width:1200px;text-align:center;top:305px;font-size:98px;font-weight:900;letter-spacing:3px;color:var(--white)}
/* headings */
.section-title{font-weight:900;font-size:44px;letter-spacing:1px}
.section-sub{font-size:15px;color:var(--accent);letter-spacing:.5px}
.center{width:1200px;text-align:center;left:0}
/* about */
.about-text{left:608px;top:903px;width:430px;font-size:15px;line-height:21px;color:#222}
/* services */
.card{position:absolute;width:218px;height:207px;background:var(--white);padding:30px 18px 0 18px}
.card h3{font-size:19px;font-weight:600;color:var(--accent);margin-bottom:10px}
.card p{font-size:15px;line-height:21px;color:#222}
.card .arrow{position:absolute;left:18px;bottom:14px;font-size:18px;color:var(--accent)}
.photo{position:absolute}
/* members */
.member{position:absolute;width:210px;text-align:center;top:2272px}
.member .portrait{width:210px;height:190px;background:linear-gradient(160deg,#e9ecef,#b9c1c9)}
.member h4{margin-top:16px;font-size:15px;font-weight:600;color:var(--accent);letter-spacing:.5px}
.member p{margin-top:8px;font-size:15px;line-height:21px;color:#222}
.member .socials{margin-top:6px;display:flex;justify-content:center;gap:4px}
.member .socials span{width:20px;height:20px;border:1.5px solid #222;border-radius:50%}
/* contact */
.contact-item{left:166px;color:var(--white);display:flex;gap:18px}
.contact-item b{display:block;font-size:18px;font-weight:600}
.contact-item span{display:block;font-size:18px;font-weight:400;line-height:25px}
.field{left:608px;width:435px;font-size:14px;color:#d5e2ef;border-bottom:1.5px solid #7fa6c8;padding-bottom:12px}
/* footer */
.foot-col{top:3346px;color:var(--white)}
.foot-col h5{font-size:16px;font-weight:600;margin-bottom:18px}
.foot-col li{list-style:none;font-size:15px;color:#cfd8e3;height:30px}
.foot-social li{display:flex;align-items:center;gap:14px}
.foot-social li i{width:14px;height:14px;border-radius:50%;background:var(--accent)}
.copyright{top:3588px;width:1200px;text-align:center;font-size:15px;color:#cfd8e3}
</style>
</head>
<body>

<svg class="backdrop" width="1200" height="3673" viewBox="0 0 1200 3673">
  <defs>
    <linearGradient id="heroGrad" x1="0" y1="0" x2="0" y2="1">
      <stop offset="0" stop-color="#0b1626"/>
      <stop offset=".45" stop-color="#0e2135"/>
      <stop offset="1" stop-color="#1b4a6d"/>
    </linearGradient>
    <linearGradient id="cityGrad" x1="0" y1="0" x2="0" y2="1">
      <stop offset="0" stop-color="#060d1a" stop-opacity="0"/>
      <stop offset=".35" stop-color="#2a2f3a"/>
      <stop offset=".6" stop-color="#1a2230"/>
      <stop offset="1" stop-color="#0b1830"/>
    </linearGradient>
    <linearGradient id="aboutGrad" x1="0" y1="0" x2="0" y2="1">
      <stop offset="0" stop-color="#dedfe1"/>
      <stop offset="1" stop-color="#f6f6f7"/>
    </linearGradient>
    <linearGradient id="contactGrad" x1="0" y1="0" x2="0" y2="1">
      <stop offset="0" stop-color="#1f5b8c"/>
      <stop offset="1" stop-color="#123a5e"/>
    </linearGradient>
    <linearGradient id="aboutPhoto" x1="0" y1="0" x2="1" y2="1">
      <stop offset="0" stop-color="#2d6d9c"/>
      <stop offset="1" stop-color="#a9c6dd"/>
    </linearGradient>
  </defs>
  <rect width="1200" height="3673" fill="url(#aboutGrad)"/>
  <polygon points="0,0 1200,0 1200,571 600,709 0,578" fill="url(#heroGrad)" role="img" aria-label="Night city skyline with glowing tower lights"/>
  <polyline points="0,584 600,716 1200,577" fill="none" stroke="#c7ccd2" stroke-width="3"/>
  <polyline points="0,578 600,709 1200,571" fill="none" stroke="#2f7bb8" stroke-width="6"/>
  <circle cx="600" cy="709" r="28" fill="#ffffff" stroke="#c7ccd2" stroke-width="2"/>
  <circle cx="600" cy="709" r="11" fill="#2f7bb8"/>

  <polygon points="157,860 247,820 260,753 340,790 488,860 488,940 420,1000 157,1045" fill="url(#aboutPhoto)" role="img" aria-label="Two business partners shaking hands in an office"/>
  <polygon points="157,1045 420,1000 488,940 488,1000 200,1090 157,1080" fill="#1e3f5d"/>
  <polygon points="170,1040 255,1005 400,1090 315,1137" fill="#0d2236"/>

  <polygon points="0,1110 600,1259 1200,1113 1200,2205 600,2055 0,2205" fill="#060d1a"/>
  <polygon points="600,1259 1200,1113 1200,1415" fill="#14304f"/>
  <rect x="0" y="1560" width="1200" height="560" fill="url(#cityGrad)" role="img" aria-label="Harbour city skyline at night reflected on water"/>
  <polygon points="0,2205 600,2055 1200,2205 1200,2694 600,2754 0,2694" fill="#ffffff"/>

  <polygon points="0,2694 600,2754 1200,2694 1200,3256 0,3256" fill="url(#contactGrad)"/>
  <polygon points="600,2754 1200,2694 1200,2820" fill="#17223f"/>
  <rect x="0" y="3256" width="1200" height="417" fill="#08101d"/>
</svg>

<!-- top bar -->
<div class="abs topbar" style="left:160px">
  <svg width="11" height="13" viewBox="0 0 11 13"><path d="M5.5 12C2 7.5 1 6 1 4.5a4.5 4.5 0 0 1 9 0C10 6 9 7.5 5.5 12z" fill="none" stroke="#c9d6e4"/><circle cx="5.5" cy="4.5" r="1.5" fill="#c9d6e4"/></svg>4120 Alder Crest Way, Suite</div>
<div class="abs topbar" style="left:383px">
  <svg width="12" height="12" viewBox="0 0 12 12"><path d="M2 1l2 0 1 3-1.5 1a7 7 0 0 0 3.5 3.5L8 7l3 1v2l-1 1C5 11 1 7 1 2z" fill="none" stroke="#c9d6e4"/></svg>1-800-555-0187</div>
<div class="abs topbar" style="left:868px">
  <svg width="12" height="10" viewBox="0 0 12 10"><rect x=".5" y=".5" width="11" height="9" fill="none" stroke="#c9d6e4"/><path d="M.5 .5l5.5 5 5.5-5" fill="none" stroke="#c9d6e4"/></svg>hello@keystonecurrent.com</div>

<!-- header -->
<div class="abs brand"><div class="brand-mark"></div><div class="brand-name">Keystone Current</div></div>
<nav class="abs nav">
  <a class="active" style="left:0">Home</a>
  <a style="left:84px">About us</a>
  <a style="left:193px">Services</a>
  <a style="left:296px">Member</a>
  <a style="left:398px">Contact us</a>
</nav>

<!-- hero -->
<div class="abs hero-kicker">HIGH - PERFORMANCE</div>
<div class="abs hero-title">SOLUTIONS</div>
<div class="btn" style="left:529px;top:423px;width:143px">READ MORE</div>

<!-- about -->
<h2 class="abs section-title" style="left:608px;top:810px">ABOUT US</h2>
<div class="abs section-sub" style="left:608px;top:867px">If you are going to use a passage of Lorem Ipsum,</div>
<p class="abs about-text">There are many variations of passages of Lorem Ipsum available, but the majority have suffered al teration in some form, by injected humour, or randomised words which don't look even slightly believable. If you are going to use a passage of Lorem Ipsum, you need to be sure there isn't anything embarrassing hidden</p>
<div class="btn" style="left:608px;top:1052px;width:141px">READ MORE</div>

<!-- services -->
<h2 class="abs section-title center" style="top:1362px;color:var(--white)">OUR SERVICES</h2>
<div class="abs section-sub center" style="top:1416px;color:var(--accent)">If you are going to use a passage of Lorem Ipsum</div>

<div class="card" style="left:157px;top:1460px"><h3>Lorem Ipsum</h3><p>There are many variations of passages of Lorem Ipsum available,</p><span class="arrow">→</span></div>
<div class="photo" style="left:375px;top:1460px;width:219px;height:207px;background:linear-gradient(135deg,#1a2f4a,#3a6f9c)" role="img" aria-label="Business handshake"></div>
<div class="card" style="left:608px;top:1460px"><h3>Lorem Ipsum</h3><p>There are many variations of passages of Lorem Ipsum available,</p><span class="arrow">→</span></div>
<div class="photo" style="left:826px;top:1460px;width:217px;height:207px;background:linear-gradient(135deg,#b7bcc2,#33587c)" role="img" aria-label="Growth chart on a digital screen"></div>

<div class="photo" style="left:157px;top:1678px;width:218px;height:207px;background:linear-gradient(135deg,#e4e1dc,#8d949b)" role="img" aria-label="Hand holding a phone with connected technology icons"></div>
<div class="card" style="left:375px;top:1678px;padding-left:26px"><h3>Lorem Ipsum</h3><p>There are many variations of passages of Lorem Ipsum available,</p><span class="arrow" style="left:26px">→</span></div>
<div class="photo" style="left:608px;top:1678px;width:218px;height:207px;background:radial-gradient(circle at 50% 60%,#e6e9f5,#5f6fa8 55%,#241c48)" role="img" aria-label="Glowing wireframe globe above an open hand"></div>
<div class="card" style="left:826px;top:1678px;padding-left:26px"><h3>Lorem Ipsum</h3><p>There are many variations of passages of Lorem Ipsum available,</p><span class="arrow" style="left:26px">→</span></div>

<div class="btn" style="left:529px;top:1911px;width:143px">VIEW ALL</div>

<!-- members -->
<h2 class="abs section-title center" style="top:2166px">MEMBER</h2>
<div class="abs section-sub center" style="top:2222px">If you are going to use a passage of Lorem Ipsum</div>

<div class="member" style="left:157px"><div class="portrait" role="img" aria-label="Portrait of a team member in a dark suit"></div><h4>JOHN DOE</h4><p>There are many variations of passages available,</p><div class="socials"><span></span><span></span><span></span></div></div>
<div class="member" style="left:384px"><div class="portrait" role="img" aria-label="Portrait of a team member holding a coffee cup"></div><h4>JOHN DOE</h4><p>There are many variations of passages available,</p><div class="socials"><span></span><span></span><span></span></div></div>
<div class="member" style="left:609px"><div class="portrait" role="img" aria-label="Portrait of a team member in a white shirt"></div><h4>JOHN DOE</h4><p>There are many variations of passages available,</p><div class="socials"><span></span><span></span><span></span></div></div>
<div class="member" style="left:833px"><div class="portrait" role="img" aria-label="Portrait of a team member holding a tablet"></div><h4>JOHN DOE</h4><p>There are many variations of passages available,</p><div class="socials"><span></span><span></span><span></span></div></div>

<div class="btn" style="left:529px;top:2618px;width:143px">VIEW ALL</div>

<!-- contact -->
<h2 class="abs section-title center" style="top:2838px;color:var(--white)">CONTACT US</h2>

<div class="abs contact-item" style="top:2934px">
  <svg width="16" height="20" viewBox="0 0 16 20" style="margin-top:8px"><path d="M8 19C3 12 1 10 1 7a7 7 0 0 1 14 0c0 3-2 5-7 12z" fill="#fff"/><circle cx="8" cy="7" r="2.5" fill="#1f5b8c"/></svg>
  <div><b>Location :</b><span>2750 Harbor Ridge Rd., Suite 210</span><span>Lakemont, CA 90000</span></div>
</div>
<div class="abs contact-item" style="top:3035px">
  <svg width="16" height="16" viewBox="0 0 16 16" style="margin-top:8px"><path d="M3 1l3 0 1.5 4-2 1.5a9 9 0 0 0 4.5 4.5L11.5 9l4 1.5v3L14 15C7 15 1 9 1 2z" fill="#fff"/></svg>
  <div><b>Phone :</b><span>+1 555 014 2290</span></div>
</div>
<div class="abs contact-item" style="top:3115px">
  <svg width="16" height="12" viewBox="0 0 16 12" style="margin-top:8px"><rect width="16" height="12" fill="#fff"/><path d="M0 0l8 6 8-6" fill="none" stroke="#1f5b8c" stroke-width="1.5"/></svg>
  <div><b>Email :</b><span>hello@keystonecurrent.com</span></div>
</div>

<div class="abs field" style="top:2938px">Your Name :</div>
<div class="abs field" style="top:2982px">Your Email :</div>
<div class="abs field" style="top:3026px">Your Phone No :</div>
<div class="abs field" style="top:3084px;padding-bottom:16px">Message :</div>
<div class="btn" style="left:608px;top:3131px;width:135px;font-size:14px;font-weight:700;letter-spacing:0">Submit Now</div>

<!-- footer -->
<div class="abs foot-col" style="left:154px"><h5>Quick Link</h5><ul><li>Home</li><li>About Us</li><li>Services</li><li>Member</li><li>Contact Us</li></ul></div>
<div class="abs foot-col" style="left:367px"><h5>Services</h5><ul><li>Lorem Ipsum</li><li>Lorem Ipsum</li><li>Lorem Ipsum</li><li>Lorem Ipsum</li></ul></div>
<div class="abs foot-col foot-social" style="left:585px"><h5>Social</h5><ul><li><i></i>Circlefeed</li><li><i></i>Chirpline</li><li><i></i>Snapgrid</li><li><i></i>Workweb</li></ul></div>
<div class="abs foot-col" style="left:803px"><h5>Newsletter</h5>
  <div style="width:240px;font-size:15px;color:#9fb0c2;border-bottom:1px solid #5d6d80;padding:4px 0 10px">Enter Your Mail ID</div>
</div>
<div class="btn" style="left:806px;top:3430px;width:143px;font-size:14px;font-weight:700">SUBSCRIBE</div>

<div class="abs copyright">© 2020&nbsp; keystone current All Rights Reserved</div>

</body>
</html>
```